Environmental Consulting Project Examples Flyer

We need a flyer designed to promote 3-4 past projects. Each project will have a picture and a paragraph description of it. The final design should convey expertise in out field to potential customers.
Updates

I uploaded a new word document with the project descriptions and a copy of one our business cards for a color/font reference.

Also the project has been guarenteed

Target Market(s)

White collar, male industrial facility managers age 40-60.

Industry/Entity Type

Consulting

Requirements
Must have
• Logo & contact info from www.corlithgrp.com

1-2 pages. A place for a photo connecting to each description.

```html
<!DOCTYPE html>
<html lang="en">
<head>
<meta charset="utf-8">
<title>Corlith Group – Project Examples</title>
<link rel="stylesheet" href="https://fonts.googleapis.com/css2?family=EB+Garamond:wght@400;500&family=Open+Sans:wght@400;600&display=swap">
<style>
  :root {
    --deep-blue: #0f4a8c;
    --mid-blue: #2a78bb;
    --sky-blue: #5ec4ee;
    --pale-cyan: #9fe0f8;
    --ink: #0b0b0b;
    --white: #ffffff;
    --frame-band: #6fb0f2;
    --frame-pale: #dff0fb;
    --contact-grey: #3a3a3a;
  }
  * { margin: 0; padding: 0; box-sizing: border-box; }
  html, body { width: 930px; height: 1200px; overflow: hidden; }
  body { font-family: "EB Garamond", Garamond, Georgia, serif; color: var(--ink); }

  .flyer {
    position: relative;
    width: 930px;
    height: 1200px;
    overflow: hidden;
    background: linear-gradient(160deg, #1b5d9f 0%, #2a73b5 35%, #3d95cf 65%, #5ac0ec 100%);
  }
  .backdrop { position: absolute; inset: 0; width: 930px; height: 1200px; }

  .brand {
    position: absolute;
    left: 128px;
    top: 50px;
    display: flex;
    align-items: center;
    gap: 14px;
  }
  .brand-mark {
    width: 58px; height: 58px;
    background: var(--sky-blue);
  }
  .brand-name {
    font-family: "EB Garamond", Garamond, Georgia, serif;
    font-size: 44px;
    font-weight: 500;
    color: var(--sky-blue);
    letter-spacing: 1px;
  }
  .contact {
    position: absolute;
    left: 56px;
    top: 130px;
    font-family: "Open Sans", Arial, sans-serif;
    font-size: 19px;
    color: var(--contact-grey);
  }
  .contact .sep { margin: 0 10px; }
  .contact .web { color: var(--sky-blue); }

  .project-title {
    position: absolute;
    color: var(--white);
    font-size: 33px;
    font-weight: 400;
    line-height: 44px;
  }
  .title-lumber { left: 53px; top: 186px; }
  .title-dam { left: 48px; top: 677px; }

  .photo-frame {
    position: absolute;
    border-radius: 18px;
    background: linear-gradient(180deg, #ffffff 0%, #f4f9fe 20%, var(--frame-band) 33%, #cfe6fb 36%, var(--frame-pale) 55%, #ffffff 100%);
    box-shadow: 0 2px 8px rgba(0,0,0,0.55);
    border: 1px solid #1f3d63;
  }
  .frame-lumber { left: 39px; top: 301px; width: 349px; height: 247px; }
  .frame-dam { left: 453px; top: 807px; width: 407px; height: 296px; }

  .photo {
    position: absolute;
    border: 1px solid #1a1a1a;
  }
  .photo-lumber {
    left: 31px; top: 33px; width: 284px; height: 183px;
    background: linear-gradient(180deg, #8c9094 0%, #b5b8ba 40%, #9c7a5c 52%, #5d5f61 65%, #4a4c4e 100%);
  }
  .photo-dam {
    left: 39px; top: 41px; width: 330px; height: 215px;
    background: linear-gradient(180deg, #3c3c3a 0%, #6b6a62 30%, #dcdcd8 45%, #8b7a5a 65%, #6d5c43 100%);
  }

  .project-text {
    position: absolute;
    font-size: 16.6px;
    line-height: 23.6px;
  }
  .text-lumber { left: 53px; top: 308px; width: 822px; }
  .text-lumber .wrap-space { float: left; width: 366px; height: 260px; }
  .text-dam { left: 48px; top: 804px; width: 390px; }
  .dropcap { font-size: 33px; line-height: 20px; font-weight: 500; }
</style>
</head>
<body>
<main class="flyer">
  <svg class="backdrop" viewBox="0 0 930 1200" aria-hidden="true">
    <defs>
      <linearGradient id="headerShade" x1="0" y1="0" x2="1" y2="0">
        <stop offset="0" stop-color="#0f4e92"/>
        <stop offset="1" stop-color="#0d3f7e"/>
      </linearGradient>
      <linearGradient id="swoosh" x1="0" y1="0" x2="1" y2="0">
        <stop offset="0" stop-color="#7fd6f6"/>
        <stop offset="0.6" stop-color="#5cc2ee"/>
        <stop offset="1" stop-color="#3b9fd9"/>
      </linearGradient>
    </defs>
    <path d="M0 0 H930 V10 C780 130 520 180 300 188 C170 192 70 186 0 180 Z" fill="url(#headerShade)"/>
    <path d="M0 180 C70 186 170 192 300 188 C520 180 780 130 930 10 V40 C800 170 560 250 340 252 C180 254 70 248 0 240 Z" fill="url(#swoosh)"/>
    <path d="M0 240 C70 248 180 254 340 252 C560 250 800 170 930 40 V150 C820 260 660 320 470 322 C330 323 190 300 0 262 Z" fill="#59bceb" opacity="0.55"/>
  </svg>

  <header>
    <div class="brand">
      <span class="brand-mark"></span>
      <span class="brand-name">Corlith Group</span>
    </div>
    <p class="contact">info@corlithgrp.com<span class="sep">|</span><span class="web">www.corlithgrp.com</span></p>
  </header>

  <section class="project">
    <h2 class="project-title title-lumber">Kestrel Bay Lumber Yard<br>Industrial Stormwater General Permit</h2>
    <div class="photo-frame frame-lumber">
      <div class="photo photo-lumber" role="img" aria-label="Photo of the paved lumber yard with stacked lumber and white warehouse buildings under an overcast sky"></div>
    </div>
    <p class="project-text text-lumber"><span class="wrap-space"></span><span class="dropcap">A</span>s part of an environmental action group’s civil lawsuit, the facility was forced to meet benchmark limits of the industrial stormwater general permit for 8 consecutive quarters. Previous quarters identified pH, turbidity, biological oxygen demand, zinc and copper as the pollutants that exceeded the benchmark limits. To solve the issue, Corlith Group utilized targeted best management practices (BMP’s) and identified and addressed the various pollutant sources. With guidance from Corlith Group, the 8 acre facility avoided the costly purchase and installation of an active treatment system while still maintaining full permit compliance.</p>
  </section>

  <section class="project">
    <h2 class="project-title title-dam">Marlow Ridge Dam<br>Construction Stormwater General Permit</h2>
    <p class="project-text text-dam"><span class="dropcap">M</span>aintaining environmental compliance with the Regional Corps of Engineers’ strict standards during construction on the banks of the City of Harwick’s water supply was a daunting task to be accomplished. Throughout the project Corlith Group kept the site in compliance. After the project was completed Corlith Group performed a final walkthrough with the Corps to ensure that no sources of pollution entered the drinking supply when the dewatered construction was put back under water.</p>
    <div class="photo-frame frame-dam">
      <div class="photo photo-dam" role="img" aria-label="Photo of dam construction site with excavators, snow-covered banks and muddy river water"></div>
    </div>
  </section>
</main>
</body>
</html>
```